River Stones, Evening Light Poster for American Indian Older Adults

We need am 11" x 17" poster designed for a health outreach project designed to reach older U.S. American Indians. The materials developed through this project will be distributed to American Indian and Alaska Native tribes, communities and tribal-serving organizations across the U.S. (more than 500 different tribes). If we find a successful design we will work with that designer to produce at least one other item we need design work for using the same look/feel and maybe other materials for this project. (more work!). The poster will include a set of facts (bulleted list on the attached document) that we would like presented in an "infographic" style. The design must be reflective of the American Indian culture and designed with older adults (65 and older) in mind. Imagery plays a strong role in the American Indian culture in the U.S. images of the heart, water, feathers, circle of life, etc. If you use photos of people they must include older adults and they must be American Indian (Native American). We prefer deep earth tones for the color scheme. The design must take into account design principles for older adults: 1. Try not to put colored font on colored background 2. Ensure high contrast for text 3. Font style should be sans serif, not cursive,decorative or heavily stylized because it is harder to read 4. Avoid using all caps 5. Don't print sideways or on top of images, shaded, backgrounds, etc. 6. All images should related specifically to the content of the text and be culturally appropriate for both older adults and American Indians. The final design should be easy to read and appeal to older American Indian adults. We need to incorporate three logos on the poster towards the bottom they should not be the center/focus of the poster. We also need to include a statement about who produced the materials- that can be very small below the logos at the bottom of the poster. We've attached the text for the poster and three logo files (note one is solid blue- we will finalize that after the document design is selected but need a placeholder for that logo.

Target Market(s)

Older adult (65 and older) American Indian and Alaska Natives and their family members in tribes, communities and tribal-serving organizations across the US

Font styles to use
Sans Serif

Requirements
Must have
• Must adhere to good design principles for older adults (listed in project description)
• Must feature culturally appropriate/targeted imagery and design look and feel

```html
<!DOCTYPE html>
<html lang="en">
<head>
<meta charset="utf-8">
<title>River Stones, Evening Light</title>
<link rel="stylesheet" href="https://fonts.googleapis.com/css2?family=Archivo+Black&family=Roboto+Condensed:wght@700;900&family=Arimo:wght@700&display=swap">
<style>
  :root{
    --blue:#2b3990;
    --blue-light:#4a5ba8;
    --red:#ed1c24;
    --white:#ffffff;
    --mist:#d9dbe9;
    --earth-dark:#8a4b25;
    --earth:#b4693a;
    --clay:#d9792e;
    --turquoise:#5fb8c2;
    --stone:#9a948c;
    --green:#2e9a48;
    --orange:#e0662b;
    --sky:#2d6fb7;
  }
  *{margin:0;padding:0;box-sizing:border-box}
  html,body{width:777px;height:1200px;overflow:hidden;background:var(--white)}
  .poster{position:relative;width:777px;height:1200px;overflow:hidden;font-family:"Roboto Condensed",sans-serif;font-weight:700}
  .abs{position:absolute}
  .header{left:0;top:0;width:777px;height:210px;background:linear-gradient(180deg,var(--blue) 0%,var(--blue-light) 100%)}
  .title{font-family:"Archivo Black",sans-serif;font-weight:400;color:var(--white);font-size:66px;line-height:1;letter-spacing:-1px}
  .title-1{left:30px;top:54px}
  .title-2{right:40px;top:130px}
  .subtitle-band{left:0;top:210px;width:777px;height:106px;background:var(--red);color:var(--white);
    font-size:36px;font-weight:700;line-height:41px;text-align:center;padding-top:13px}
  .facts{left:0;top:316px;width:777px;height:594px;background:linear-gradient(180deg,var(--mist) 0%,var(--white) 45%,var(--white) 100%)}
  .map{left:20px;top:324px;width:352px;height:244px;background:var(--red);border-radius:40px 90px 110px 60px}
  .map-text{left:20px;top:356px;width:340px;text-align:center;color:var(--white);line-height:1}
  .map-text .big{font-size:58px;font-weight:900}
  .map-text .mid{font-size:25px}
  .map-text .name{font-size:50px;font-weight:900}
  .map-text .small{font-size:25px;padding-left:100px}
  .divider-v{left:384px;top:396px;width:10px;height:416px;
    background:linear-gradient(180deg,var(--earth-dark) 0%,var(--clay) 25%,var(--turquoise) 45%,var(--earth) 65%,var(--clay) 85%,var(--earth-dark) 100%)}
  .divider-h{left:176px;top:572px;width:424px;height:10px;
    background:linear-gradient(90deg,var(--earth-dark) 0%,var(--clay) 25%,var(--turquoise) 45%,var(--earth) 65%,var(--clay) 85%,var(--earth-dark) 100%)}
  .stat{text-align:center;line-height:1}
  .red{color:var(--red)}
  .rank{left:420px;top:364px;width:340px}
  .rank .word{font-size:60px;font-weight:900;color:var(--red)}
  .rank .mid{font-size:25px;color:var(--blue);margin-top:4px}
  .rank .num{font-size:76px;font-weight:900;color:var(--red)}
  .rank .tail{font-size:26px;color:var(--blue);margin-top:4px}
  .ratio{font-size:31px;color:var(--blue)}
  .ratio-left{left:60px;top:600px;width:200px}
  .ratio-right{left:472px;top:598px;width:220px}
  .people{left:96px;top:634px}
  .age-line{left:60px;top:752px;width:300px;display:flex;align-items:flex-end;gap:8px}
  .age-line .words{font-size:29px;color:var(--blue);padding-bottom:10px}
  .age-line .num{font-size:92px;font-weight:900;color:var(--red);line-height:.82}
  .left-tail{left:40px;top:826px;width:330px}
  .left-tail .mid{font-size:30px;color:var(--blue)}
  .left-tail .name{font-size:54px;font-weight:900;color:var(--red);margin-top:2px}
  .elders-art{left:494px;top:632px;width:172px;height:84px;
    background:linear-gradient(90deg,var(--stone) 0%,var(--stone) 22%,var(--earth) 38%,var(--clay) 50%,var(--earth) 62%,var(--stone) 78%,var(--stone) 100%);border-radius:6px}
  .right-tail{left:420px;top:710px;width:340px}
  .right-tail .group{font-size:32px;font-weight:900;color:var(--red)}
  .right-tail .row{display:flex;justify-content:center;align-items:flex-end;gap:10px;margin-top:2px}
  .right-tail .row .words{font-size:31px;color:var(--blue);padding-bottom:10px}
  .right-tail .row .num{font-size:92px;font-weight:900;color:var(--red);line-height:.82}
  .right-tail .mid{font-size:31px;color:var(--blue);margin-top:6px}
  .right-tail .name{font-size:54px;font-weight:900;color:var(--red);margin-top:2px}
  .callout{left:0;top:910px;width:777px;height:202px;background:var(--blue)}
  .callout-red{left:376px;top:920px;width:401px;height:192px}
  .risk{left:44px;top:926px;width:344px;color:var(--white);font-family:"Arimo",sans-serif;font-weight:700;font-size:25px;line-height:27.5px;text-align:center}
  .action{left:436px;top:944px;width:316px;color:var(--white);font-family:"Arimo",sans-serif;font-weight:700;font-size:25px;line-height:27.5px;text-align:center}
  .partners{left:0;top:1112px;width:777px;height:72px;background:var(--white);display:flex;align-items:center;justify-content:space-around;padding:0 40px}
  .partner{font-family:"Arimo",sans-serif;font-weight:700;font-size:18px;display:flex;align-items:center;gap:8px}
  .partner .mark{width:18px;height:18px;display:inline-block}
  .partner-kestrel{color:var(--orange)}
  .partner-kestrel .mark{background:var(--orange);border-radius:50%}
  .partner-council{color:var(--green)}
  .partner-office{color:var(--sky)}
  .partner-office .mark{background:var(--sky)}
  .base-strip{left:0;top:1184px;width:777px;height:16px;background:var(--blue)}
</style>
</head>
<body>
<main class="poster">
  <header class="abs header"></header>
  <h1 class="abs title title-1">River Stones,</h1>
  <h1 class="abs title title-2">Evening Light…</h1>
  <div class="abs subtitle-band">The River of Life Flows Through<br>the Heart, Protecting the Mind and Body</div>

  <section class="abs facts"></section>
  <div class="abs map" role="img" aria-label="Red silhouette map of the United States"></div>
  <div class="abs map-text">
    <div><span class="big">5.7</span> <span class="mid">million</span></div>
    <div class="mid">Americans have</div>
    <div class="name">Alzheimer’s</div>
    <div class="small">disease</div>
  </div>

  <div class="abs divider-v" role="img" aria-label="Vertical woven arrow pattern band in brown, orange and turquoise"></div>
  <div class="abs divider-h" role="img" aria-label="Horizontal woven arrow pattern band in brown, orange and turquoise"></div>

  <div class="abs stat rank">
    <div class="word">Alzheimer’s</div>
    <div class="mid">is the</div>
    <div class="num">6th</div>
    <div class="tail">leading cause of death</div>
  </div>

  <div class="abs stat ratio ratio-left">1 out 10</div>
  <svg class="abs people" width="150" height="134" viewBox="0 0 150 134" aria-label="Ten people, one highlighted">
    <defs>
      <g id="person"><circle cx="11" cy="6" r="6"/><rect x="2" y="14" width="18" height="26" rx="4"/><rect x="5" y="34" width="5" height="24"/><rect x="12" y="34" width="5" height="24"/></g>
    </defs>
    <g fill="#2b3990">
      <use href="#person" x="0" y="10"/><use href="#person" x="32" y="10"/>
      <use href="#person" x="96" y="10"/><use href="#person" x="128" y="10"/>
      <use href="#person" x="0" y="74"/><use href="#person" x="32" y="74"/><use href="#person" x="64" y="74"/>
      <use href="#person" x="96" y="74"/><use href="#person" x="128" y="74"/>
    </g>
    <g fill="#ed1c24"><use href="#person" transform="translate(60 0) scale(1.25)"/></g>
  </svg>
  <div class="abs age-line"><span class="words">people age</span><span class="num">65</span></div>
  <div class="abs stat left-tail">
    <div class="mid">and older has</div>
    <div class="name">Alzheimer’s</div>
  </div>

  <div class="abs stat ratio ratio-right">1 out of 3</div>
  <div class="abs elders-art" role="img" aria-label="Illustration of three American Indian elders in feather headdresses, in grey, brown and orange tones"></div>
  <div class="abs stat right-tail">
    <div class="group">American Indians</div>
    <div class="row"><span class="words">over</span><span class="num">65</span><span class="words">develop</span></div>
    <div class="mid"><span class="red">dementia</span>, including</div>
    <div class="name">Alzheimer’s</div>
  </div>

  <section class="abs callout"></section>
  <svg class="abs callout-red" viewBox="0 0 401 192" preserveAspectRatio="none" aria-hidden="true">
    <polygon points="70,0 401,0 401,192 0,192 40,96" fill="#ed1c24"/>
  </svg>
  <p class="abs risk">Elders with diabetes, heart disease, or high blood pressure have a much higher risk of developing Alzheimer’s or other dementias</p>
  <p class="abs action">Make an appointment with your doctor today to talk about how to keep your mind and heart healthy.</p>

  <footer class="abs partners">
    <span class="partner partner-kestrel"><span class="mark"></span>Kestrel Health</span>
    <span class="partner partner-council">Council for Elder Wellbeing</span>
    <span class="partner partner-office"><span class="mark"></span>Public Wellness Office</span>
  </footer>
  <div class="abs base-strip"></div>
</main>
</body>
</html>
```